Premium modern eliquids labels 84.5 x 80 mm

I am looking for modern graphics for the labels of a new eliquid line that will have 4 different types of eliquids. It will have a tobacco one (brown colours maybe), a fruity one (bright colours maybe), a minty one (green colours maybe) and a creamy one (beige colours maybe).
I will need one of them to see how the design is, that design will have to be adapted to the other 3 colours of the label.
The brand logo is attached. I also attached a sample of what is mandatory to write on the label, you can change size, place and font of what is written, the only thing that cannot be reduced is the yellow parts. I attach the bottle that we will use.The size of the label is 84.5 x 80 mm (base x height).

Target Market(s)

vapers

Requirements
Must have
• My project must have one of the labels.

```html
<!DOCTYPE html>
<html lang="it">
<head>
<meta charset="utf-8">
<title>Velvet Essence – Tobacco eliquid label</title>
<link href="https://fonts.googleapis.com/css2?family=Arimo:wght@400;700&family=Yellowtail&display=swap" rel="stylesheet">
<style>
  :root {
    --label-brown: #4a2c17;
    --ink-white: #ffffff;
    --badge-yellow: #f5b21a;
    --brand-blue: #6fb8e6;
    --leaf-light: #d9d98a;
    --leaf-dark: #7f9a4e;
  }
  * { margin: 0; padding: 0; box-sizing: border-box; }
  html, body { width: 1200px; height: 1137px; overflow: hidden; background: var(--label-brown); }
  .label {
    position: relative; width: 1200px; height: 1137px;
    background: var(--label-brown); color: var(--ink-white);
    font-family: "Arimo", Arial, sans-serif;
  }
  .block { position: absolute; font-size: 20px; line-height: 29px; }
  .ingredients { left: 18px; top: 56px; text-transform: uppercase; }
  .batch { left: 18px; top: 366px; }
  .producer { left: 18px; top: 863px; }
  .instructions { left: 876px; top: 60px; font-weight: 700; }
  .brand {
    position: absolute; left: 380px; top: 180px; width: 440px;
    display: flex; align-items: center; justify-content: center; gap: 14px;
    color: var(--brand-blue); font-weight: 700; font-size: 46px; letter-spacing: 1px;
  }
  .brand-dot { width: 26px; height: 26px; border-radius: 50%; background: var(--brand-blue); }
  .range {
    position: absolute; left: 400px; top: 380px; width: 400px; text-align: center;
    font-weight: 700; font-size: 41px;
  }
  .try-more { position: absolute; left: 874px; top: 304px; font-weight: 700; font-size: 20px; }
  .flavour-art { position: absolute; }
  .art-fruit { left: 851px; top: 350px; width: 208px; height: 74px; border-radius: 40px;
    background: linear-gradient(90deg, #f2c12e, #e9573a, #f0a52a, #9bc54a); }
  .art-mint { left: 880px; top: 452px; width: 142px; height: 96px; border-radius: 50%;
    background: radial-gradient(circle, #7cc25a, #3f8a35); }
  .art-vanilla { left: 839px; top: 574px; width: 226px; height: 88px; border-radius: 44px;
    background: linear-gradient(90deg, #3a2214, #f4d33b 45%, #f7e27a 55%, #3a2214); }
  .flavour-name {
    position: absolute; width: 120px; text-align: center;
    font-weight: 700; font-size: 20px; line-height: 29px;
  }
  .name-fruit { left: 1068px; top: 357px; }
  .name-mint { left: 1068px; top: 470px; }
  .name-vanilla { left: 1068px; top: 589px; }
  .art-leaf { position: absolute; left: 436px; top: 660px; width: 326px; height: 300px;
    border-radius: 50% 50% 45% 55%;
    background: radial-gradient(ellipse at 55% 40%, var(--leaf-light), var(--leaf-dark)); }
  .flavour-title {
    position: absolute; left: 400px; top: 1010px; width: 400px; text-align: center;
    font-family: "Yellowtail", cursive; font-size: 56px; line-height: 80px;
  }
  .badge {
    position: absolute; background: var(--badge-yellow); color: var(--ink-white);
    font-weight: 700; border-radius: 10px; text-align: center;
  }
  .badge-collect { left: 869px; width: 160px; height: 60px; font-size: 19px; line-height: 23px; padding-top: 7px; }
  .badge-code { left: 1041px; width: 132px; height: 49px; font-size: 33px; line-height: 49px; }
  .collect-label { top: 734px; } .collect-bottle { top: 859px; }
  .code-label { top: 802px; } .code-bottle { top: 926px; }
  .part { position: absolute; left: 1046px; font-size: 20px; }
  .part-label { top: 752px; } .part-bottle { top: 877px; }
  .net { position: absolute; left: 879px; top: 982px; font-weight: 700; font-size: 27px; }
  .icon { position: absolute; }
  .icon-recycle { left: 996px; top: 1028px; }
  .icon-bin { left: 1094px; top: 1002px; }
</style>
</head>
<body>
<main class="label">
  <div class="block ingredients">Ingredienti:<br>Glicole, propilenico<br>sostanze, aromatizzanti</div>

  <div class="brand"><span class="brand-dot"></span><span>VELVET ESSENCE</span></div>

  <div class="block instructions">ISTRUZIONI D’USO:<br>Agitare bene prima<br>dell’utilizzo.<br>Diluire nelle percentuali<br>consigliate sul nostro sito.<br>Conservare in luogo fresco<br>e asciutto</div>

  <div class="block batch">L.SH20 - 001-PES-D.<br>PROD.22-04-2022<br>D.SC.21-04-2024</div>

  <div class="range">eliquids</div>

  <div class="try-more">PROVA ALTRI GUSTI:</div>
  <div class="flavour-art art-fruit" role="img" aria-label="Splash of mixed fruit slices"></div>
  <div class="flavour-name name-fruit">Citrus<br>Burst</div>
  <div class="flavour-art art-mint" role="img" aria-label="Fresh mint leaves"></div>
  <div class="flavour-name name-mint">Cool<br>Breeze</div>
  <div class="flavour-art art-vanilla" role="img" aria-label="Vanilla flower with vanilla pods"></div>
  <div class="flavour-name name-vanilla">Sweet<br>Cream</div>

  <div class="art-leaf" role="img" aria-label="Illustration of dried tobacco leaves"></div>
  <div class="flavour-title">Tobacco</div>

  <div class="badge badge-collect collect-label">RACCOLTA<br>PLASTICA</div>
  <div class="part part-label">ETICHETTA</div>
  <div class="badge badge-code code-label">PAP 5</div>
  <div class="badge badge-collect collect-bottle">RACCOLTA<br>PLASTICA</div>
  <div class="part part-bottle">FLACONE</div>
  <div class="badge badge-code code-bottle">PET 1</div>

  <div class="net">20ML NET</div>

  <svg class="icon icon-recycle" width="82" height="80" viewBox="0 0 82 80" aria-hidden="true">
    <g fill="none" stroke="#ffffff" stroke-width="5" stroke-linejoin="round">
      <path d="M30 10 L41 4 L52 22"/><path d="M48 14 L53 24 L42 24"/>
      <path d="M66 36 L78 58 L62 72"/><path d="M68 64 L60 72 L66 62"/>
      <path d="M44 74 L16 74 L4 54"/><path d="M12 44 L4 54 L16 56"/>
      <path d="M24 16 L12 36"/><path d="M60 28 L68 42"/><path d="M26 74 L54 74"/>
    </g>
  </svg>

  <svg class="icon icon-bin" width="80" height="106" viewBox="0 0 80 106" aria-hidden="true">
    <g fill="#ffffff">
      <circle cx="58" cy="10" r="9"/>
      <path d="M48 22 h20 v44 h-6 v38 h-8 v-38 h-6 z"/>
      <path d="M48 26 L32 44 l4 4 L50 34 z"/>
      <rect x="28" y="52" width="4" height="6"/>
    </g>
    <path d="M4 58 h34 l-5 46 h-24 z" fill="none" stroke="#ffffff" stroke-width="5" stroke-linejoin="round"/>
    <path d="M16 68 v28 M26 68 v28" stroke="#ffffff" stroke-width="4"/>
  </svg>

  <div class="block producer">PRODOTTO<br>E CONFEZIONATO<br>DA Nordline srl<br>Via Lago 18<br>10100 Borgo Alto<br>P.i.00000000000<br>Tel. +39 000 0000000<br>info@nordline.it</div>
</main>
</body>
</html>
```